Top header for website

Header for website Size is 1000px x 120px
I have CS5 so will need the source files photoshop, illustrator etc, so I can change text and photos.
Photos attached, includes example header and screenshot of eg site
Brief:
I need a website header for golfers where I can change the photos and their name.
The header needs to have these things.
- pictures of the golfer (use from pics attached)
- Their name
- Also under there name is smaller text I need a line of text you can just say "Offical Website" in your e.g to me
so for example you should have
Dale Fenwick
Offical Website
And some photos that are blended with some nice golf background or some grass or other ideas that you come up with that will look better than mine I'm sure :)
Size is 1000px x 120px
It needs to look professional and blend in nicely. I don't mind how many photos are used maybe 1-4?
The text needs to look professional too but not boring.
The header you create will be used on a website for a Professional Golfer (tour pro) their job is golf, their website needs to showcase them and promote them as best as possible.
As I said above I will need to swap photos easily and edit the text so will need the source files.
So a important point here. I guess there is no need to blend or do anything to the photos you add as I will actually need to change the photos and just need a simple template that I can swap photos and edit their name.
Ultimately I would like 3 versions of the header done and source files for all 3 so I can give them(the golfers) a choice of header type.
See how you go.
Remember that the header must have the ability for me to easily swap images and of course change the text.
My goal is to use the same header for each golfer but obviously with their images and their name.
I have CS5 so will need the source files photoshop, illustrator etc
2 example headers are attached to show you my attempts :) Please do something better.
I don't want any flash.

```html
<!DOCTYPE html>
<html lang="en">
<head>
<meta charset="utf-8">
<title>Dale Fenwick – Official Website</title>
<link rel="stylesheet" href="https://fonts.googleapis.com/css2?family=Open+Sans:wght@300;400;700&family=PT+Sans:wght@400;700&display=swap">
<style>
  :root {
    --backdrop: #3a3e40;
    --header-black: #0b0b0b;
    --nav-top: #4f95f6;
    --nav-mid: #2f7bee;
    --nav-bottom: #5fa3fb;
    --page: #f5f6f7;
    --panel: #ffffff;
    --panel-border: #dcdfe2;
    --accent: #3a7fe0;
    --rule: #3f80e4;
    --text: #2b2b2b;
    --muted: #555a5e;
    --cell: #eceff1;
    --cell-head: #dfe3e5;
    --white: #ffffff;
  }
  * { box-sizing: border-box; margin: 0; padding: 0; }
  html, body { width: 1200px; height: 818px; overflow: hidden; }
  body { background: var(--backdrop); font-family: "PT Sans", Arial, sans-serif; color: var(--text); position: relative; }

  .site { position: absolute; left: 44px; top: 37px; width: 1108px; height: 781px; background: var(--page); overflow: hidden; }

  .site-header { position: absolute; left: 0; top: 0; width: 1108px; height: 135px; background: var(--header-black); }
  .portrait { position: absolute; left: 11px; top: 10px; width: 113px; height: 114px; border: 3px solid var(--white);
    background: linear-gradient(160deg, #d9d4cc 0%, #b7876a 45%, #3b3026 100%); }
  .header-photo { position: absolute; right: 0; top: 0; width: 380px; height: 135px;
    background: linear-gradient(90deg, var(--header-black) 0%, #1d2a12 25%, #3f6a22 55%, #5e8f2c 80%, #6f9b33 100%); }
  .golfer-name { position: absolute; left: 145px; top: 26px; font-family: "Open Sans", Arial, sans-serif; font-weight: 300;
    font-size: 45px; letter-spacing: 0.5px; color: var(--white); text-transform: uppercase; line-height: 1; }
  .golfer-tagline { position: absolute; left: 146px; top: 80px; font-family: "Open Sans", Arial, sans-serif; font-weight: 700;
    font-size: 16px; color: var(--white); text-transform: uppercase; }

  .main-nav { position: absolute; left: 0; top: 135px; width: 1108px; height: 65px;
    background: linear-gradient(180deg, var(--nav-top) 0%, var(--nav-mid) 55%, var(--nav-bottom) 100%); }
  .main-nav a { position: absolute; top: 15px; color: var(--white); font-size: 17px; text-decoration: none; letter-spacing: 0.2px; }

  .slider { position: absolute; left: 22px; top: 223px; width: 741px; height: 335px; background: var(--panel); border: 1px solid var(--panel-border); }
  .slide-image { position: absolute; left: 12px; top: 12px; width: 717px; height: 309px;
    background: linear-gradient(180deg, #3c4a25 0%, #5b6b38 35%, #dfe1dc 60%, #e8e9e6 100%); }
  .slider-arrow { position: absolute; top: 368px; width: 34px; height: 40px; }
  .slider-arrow.prev { left: 7px; }
  .slider-arrow.next { left: 746px; }

  .section-title { position: absolute; font-size: 16px; font-weight: 400; color: var(--accent); }
  .section-rule { position: absolute; height: 2px; background: var(--rule); }

  .article { position: absolute; left: 22px; top: 644px; width: 741px; height: 160px; background: var(--panel); border: 1px solid var(--panel-border); }
  .article-title { position: absolute; left: 11px; top: 24px; font-size: 22px; font-weight: 400; color: var(--text); }
  .article-line { position: absolute; left: 11px; right: 11px; height: 1px; background: #e6e8ea; }
  .article-date { position: absolute; left: 11px; top: 77px; font-size: 12px; color: var(--muted); }
  .article-excerpt { position: absolute; left: 11px; top: 120px; font-size: 12px; color: var(--muted); }

  .like-widget { position: absolute; left: 786px; top: 277px; display: flex; align-items: center; gap: 8px; font-size: 12px; color: var(--muted); }
  .like-button { display: flex; align-items: center; height: 25px; padding: 0 6px; background: #f4f6f9; border: 1px solid #c9d0da; color: #3b5a8c; font-size: 12px; }
  .like-square { width: 10px; height: 10px; background: #3b5a8c; }

  .scores { position: absolute; left: 783px; top: 379px; width: 300px; table-layout: fixed; border-collapse: separate; border-spacing: 3px; font-size: 12px; color: var(--muted); }
  .scores th { background: var(--cell-head); font-weight: 400; font-size: 12px; color: #7a8085; height: 20px; text-transform: uppercase; }
  .scores td { background: var(--cell); vertical-align: top; padding: 5px 6px; line-height: 14px; }
  .scores td.pos, .scores td.score { text-align: center; padding-left: 2px; padding-right: 2px; }
</style>
</head>
<body>
<div class="site">
  <header class="site-header">
    <div class="portrait" role="img" aria-label="Portrait of the golfer wearing a white cap"></div>
    <div class="header-photo" role="img" aria-label="Golfer finishing a swing on a green course"></div>
    <h1 class="golfer-name">Dale Fenwick</h1>
    <p class="golfer-tagline">Offical Website</p>
  </header>

  <nav class="main-nav">
    <a href="#" style="left:66px">HOME</a>
    <a href="#" style="left:160px">ABOUT</a>
    <a href="#" style="left:259px">NEWS</a>
    <a href="#" style="left:352px">RESULTS</a>
    <a href="#" style="left:463px">SCHEDULE</a>
    <a href="#" style="left:589px">GALLERY</a>
    <a href="#" style="left:702px">BLOG</a>
    <a href="#" style="left:791px">CONTACT</a>
  </nav>

  <section class="slider">
    <div class="slide-image" role="img" aria-label="Golfer teeing off in front of spectators at a tournament"></div>
  </section>
  <svg class="slider-arrow prev" viewBox="0 0 34 40" aria-hidden="true">
    <rect x="0" y="0" width="34" height="32" fill="#2f7bee"/>
    <polygon points="0,32 10,32 10,40" fill="#1b4fa0"/>
    <polyline points="20,8 12,16 20,24" fill="none" stroke="#fff" stroke-width="4"/>
  </svg>
  <svg class="slider-arrow next" viewBox="0 0 34 40" aria-hidden="true">
    <rect x="0" y="0" width="34" height="32" fill="#2f7bee"/>
    <polygon points="24,32 34,32 24,40" fill="#1b4fa0"/>
    <polyline points="14,8 22,16 14,24" fill="none" stroke="#fff" stroke-width="4"/>
  </svg>

  <h2 class="section-title" style="left:22px;top:590px">Latest Articles</h2>
  <div class="section-rule" style="left:22px;top:620px;width:741px"></div>

  <article class="article">
    <h3 class="article-title">Kestrel Bay Masters</h3>
    <div class="article-line" style="top:67px"></div>
    <p class="article-date">Jan - 11 - 2013</p>
    <div class="article-line" style="top:98px"></div>
    <p class="article-excerpt">testing new post</p>
  </article>

  <h2 class="section-title" style="left:786px;top:233px">Clubhouse</h2>
  <div class="section-rule" style="left:786px;top:263px;width:299px"></div>
  <div class="like-widget">
    <span class="like-button">Like</span>
    <span class="like-square"></span>
    <span>10 people like this.</span>
  </div>

  <h2 class="section-title" style="left:786px;top:335px">Latest Scores</h2>
  <div class="section-rule" style="left:786px;top:365px;width:299px"></div>

  <table class="scores">
    <colgroup><col style="width:114px"><col style="width:43px"><col style="width:61px"><col style="width:65px"></colgroup>
    <tr><th>Tournament</th><th>Pos</th><th>Score</th><th>Money</th></tr>
    <tr style="height:68px"><td>Riverbend Tour Championship<br>Nov 29 - Dec 02, 2012</td><td class="pos">35</td><td class="score">69-75-72-71<br>287<br>(-1)</td><td>$850</td></tr>
    <tr style="height:68px"><td>2012 Harbourline Open<br>Nov 22 - Dec 25, 2012</td><td class="pos">56</td><td class="score">79-72-76-70<br>297<br>(+9)</td><td>$914.4</td></tr>
    <tr style="height:68px"><td>Kestrel Bay Masters<br>Nov 15 - Nov 18, 2012</td><td class="pos">CUT</td><td class="score">77-77--<br>154<br>(+10)</td><td></td></tr>
    <tr style="height:82px"><td>Millbrook Copper Kettle Pro-Am<br>Oct 3 - Oct 4, 2012</td><td class="pos">6</td><td class="score">68-67<br>135<br>(-3)</td><td>$669.4</td></tr>
    <tr style="height:67px"><td>Southvale Tour Pro-Am Championship<br>Mar 29 - Apr 1, 2012</td><td class="pos">CUT</td><td class="score">76-71<br>147<br>(+3)</td><td></td></tr>
  </table>
</div>
</body>
</html>
```